Concierge Healthcare Business Card Design and Logo

We need a logo and business card design for a new company called "Sound Keeper". We will provide concierge audiological care, hearing aids, hearing exams, custom hearing protection etc to patients in the comfort of their homes and offices. We would like a sleek and modern design preferably with an Ear related logo.

Target Market(s)

People with hearing loss, Hunters, Musicians
My usual clientele are older individuals so usually 50+ years old

Industry/Entity Type

Health Care

Contact Information for Business Card

Clara Whitfield, AuD
Audiologist
512-418-2967
soundkeeper@mailvista.net
www.soundkeeperclinic.net

Logo Text

Sound Keeper

Number of Pages Required

3 page

```html
<!DOCTYPE html>
<html lang="en">
<head>
<meta charset="utf-8">
<title>Sound Keeper – Business Card</title>
<link rel="stylesheet" href="https://fonts.googleapis.com/css2?family=Open+Sans:wght@400;600;700&display=swap">
<style>
  :root {
    --ink: #272733;
    --paper: #f5f7f6;
    --amber: #fdb94a;
    --amber-dark: #e9a136;
    --page: #ffffff;
    --edge: #8a8a8a;
  }
  * { box-sizing: border-box; margin: 0; padding: 0; }
  html, body {
    width: 1200px; height: 596px; overflow: hidden;
    background: var(--page);
    font-family: "Open Sans", Verdana, sans-serif;
  }
  .canvas { position: relative; width: 1200px; height: 596px; }
  .card { position: absolute; width: 514px; height: 314px; overflow: hidden; }

  /* Front */
  .card-front { left: 64px; top: 142px; background: var(--ink); outline: 1px solid var(--edge); }
  .front-panel { position: absolute; inset: 0; }
  .brand {
    position: absolute; left: 62px; top: 140px;
    display: flex; align-items: center; gap: 10px;
  }
  .brand-dot { width: 34px; height: 34px; border-radius: 50%; background: var(--amber); }
  .brand-name {
    color: var(--amber); font-weight: 700; font-size: 21px;
    letter-spacing: 1px; text-transform: uppercase;
  }
  .name-band {
    position: absolute; left: 266px; top: 75px; width: 248px; height: 43px;
    background: var(--amber); color: var(--ink);
    font-weight: 700; font-size: 17px; letter-spacing: 0.3px;
    display: flex; align-items: center; justify-content: center;
  }
  .role {
    position: absolute; left: 344px; top: 121px;
    font-size: 14px; letter-spacing: 1.2px; color: var(--ink);
  }
  .contact-list { position: absolute; left: 301px; top: 191px; list-style: none; }
  .contact-list li {
    display: flex; align-items: center; gap: 10px;
    height: 28px; font-size: 12.5px; color: #111;
  }
  .icon-badge {
    width: 20px; height: 20px; border-radius: 50%;
    background: var(--amber); display: flex; align-items: center; justify-content: center;
    flex: none;
  }
  .icon-badge svg { width: 12px; height: 12px; fill: #fff; }

  /* Back */
  .card-back { left: 622px; top: 135px; background: var(--ink); }
  .services { position: absolute; left: 104px; top: 56px; color: var(--amber); }
  .services h2 { font-size: 19px; font-weight: 700; letter-spacing: 0.5px; margin-bottom: 6px; }
  .services ul { list-style: none; }
  .services li {
    display: flex; align-items: center; gap: 14px;
    height: 31px; font-size: 16px; font-weight: 400;
  }
  .bullet { width: 10px; height: 10px; border-radius: 50%; border: 2px solid var(--amber); flex: none; margin-left: 2px; }
  .services .more { padding-left: 28px; font-size: 16px; }
  .footer-band {
    position: absolute; left: 0; bottom: 0; width: 100%; height: 52px;
    background: var(--amber);
    display: flex; align-items: center; justify-content: center; gap: 12px;
  }
  .footer-item { display: flex; align-items: center; gap: 5px; font-size: 11px; color: var(--ink); }
  .footer-item .icon-badge { background: var(--ink); width: 18px; height: 18px; }
  .footer-item .icon-badge svg { width: 11px; height: 11px; fill: var(--amber); }
</style>
</head>
<body>
<svg width="0" height="0" style="position:absolute" aria-hidden="true">
  <defs>
    <symbol id="icon-phone" viewBox="0 0 24 24"><path d="M6.6 10.8a15.1 15.1 0 0 0 6.6 6.6l2.2-2.2a1 1 0 0 1 1-.25 11.4 11.4 0 0 0 3.6.57 1 1 0 0 1 1 1V20a1 1 0 0 1-1 1A17 17 0 0 1 3 4a1 1 0 0 1 1-1h3.5a1 1 0 0 1 1 1c0 1.25.2 2.45.57 3.6a1 1 0 0 1-.25 1z"/></symbol>
    <symbol id="icon-mail" viewBox="0 0 24 24"><path d="M2 5h20v14H2z M3.5 6.5 12 13l8.5-6.5" fill-rule="evenodd"/><path d="M3 6l9 7 9-7" stroke="#000" stroke-opacity=".25" stroke-width="1.6" fill="none"/></symbol>
    <symbol id="icon-globe" viewBox="0 0 24 24"><path d="M12 2a10 10 0 1 0 0 20 10 10 0 0 0 0-20zm-1 17.9A8 8 0 0 1 4.1 11H8a16 16 0 0 0 3 8.9zM8 9H4.3A8 8 0 0 1 11 4.1 16 16 0 0 0 8 9zm5 10.9A16 16 0 0 0 16 11h3.9a8 8 0 0 1-6.9 8.9zM16 9a16 16 0 0 0-3-4.9A8 8 0 0 1 19.7 9zM10 11h4a14 14 0 0 1-2 6.5A14 14 0 0 1 10 11zm0-2a14 14 0 0 1 2-4.5A14 14 0 0 1 14 9z"/></symbol>
  </defs>
</svg>

<main class="canvas">
  <section class="card card-front" aria-label="Business card front">
    <svg class="front-panel" viewBox="0 0 514 314" aria-hidden="true">
      <polygon points="366,0 514,0 514,314 234,314" fill="var(--paper)"/>
      <polygon points="266,118 316,118 300,154" fill="var(--amber-dark)"/>
    </svg>
    <div class="brand">
      <span class="brand-dot"></span>
      <span class="brand-name">Sound Keeper</span>
    </div>
    <h1 class="name-band">Clara Whitfield, AuD</h1>
    <p class="role">Audiologist</p>
    <ul class="contact-list">
      <li><span class="icon-badge"><svg><use href="#icon-phone"/></svg></span>512-418-2967</li>
      <li><span class="icon-badge"><svg><use href="#icon-mail"/></svg></span>soundkeeper@mailvista.net</li>
      <li><span class="icon-badge"><svg><use href="#icon-globe"/></svg></span>www.soundkeeperclinic.net</li>
    </ul>
  </section>

  <section class="card card-back" aria-label="Business card back">
    <div class="services">
      <h2>We provide</h2>
      <ul>
        <li><span class="bullet"></span>Concierge audiological care</li>
        <li><span class="bullet"></span>Hearing aids</li>
        <li><span class="bullet"></span>Hearing exams</li>
        <li><span class="bullet"></span>Custom hearing protection</li>
      </ul>
      <p class="more">...</p>
    </div>
    <div class="footer-band">
      <span class="footer-item"><span class="icon-badge"><svg><use href="#icon-phone"/></svg></span>512-418-2967</span>
      <span class="footer-item"><span class="icon-badge"><svg><use href="#icon-mail"/></svg></span>soundkeeper@mailvista.net</span>
      <span class="footer-item"><span class="icon-badge"><svg><use href="#icon-globe"/></svg></span>www.soundkeeperclinic.net</span>
    </div>
  </section>
</main>
</body>
</html>
```